Business Card for Dental Office

Our office is in the Hillcrest section of San Diego, California which is a well-established area. Maybe the back can be a map of our office location

```html
<!DOCTYPE html>
<html lang="en">
<head>
<meta charset="utf-8">
<title>Elmfield Dental – Business Card</title>
<link rel="stylesheet" href="https://fonts.googleapis.com/css2?family=Lato:wght@400;700&display=swap">
<style>
  :root {
    --stage: #2b2b2b;
    --card-light: #f4f4f4;
    --card-mid: #e2e2e2;
    --band: #9a9a9a;
    --band-dark: #8a8a8a;
    --ink: #6f6f6f;
    --ink-soft: #8c8c8c;
    --ink-strong: #5e5e5e;
    --pattern-a: #8d8d8d;
    --pattern-b: #6b6b6b;
    --white: #ffffff;
  }
  * { box-sizing: border-box; margin: 0; padding: 0; }
  html, body {
    width: 1200px; height: 997px; overflow: hidden;
    background: var(--stage);
    font-family: "Lato", sans-serif;
  }
  .stage { position: relative; width: 1200px; height: 997px; }

  .card {
    position: absolute; left: 300px;
    width: 600px; height: 343px;
    border-radius: 4px; overflow: hidden;
    box-shadow: 0 14px 30px rgba(0,0,0,.45);
  }

  /* Back side */
  .card-back { top: 120px; }
  .back-pattern {
    position: absolute; inset: 0;
    background: linear-gradient(135deg, var(--pattern-a) 0%, var(--pattern-b) 55%, var(--pattern-a) 100%);
  }
  .back-brand {
    position: absolute; inset: 0;
    display: flex; align-items: center; justify-content: center; gap: 12px;
  }
  .brand-dot {
    width: 14px; height: 14px; border-radius: 50%;
    background: var(--white);
  }
  .back-brand .brand-name {
    color: var(--white); font-size: 40px; font-weight: 400; letter-spacing: .5px;
  }

  /* Front side */
  .card-front {
    top: 513px;
    background: linear-gradient(160deg, var(--card-light) 0%, var(--card-mid) 100%);
  }
  .front-brand {
    position: absolute; left: 40px; top: 118px;
    display: flex; align-items: center; gap: 10px;
  }
  .front-brand .brand-dot { background: var(--ink); width: 12px; height: 12px; }
  .front-brand .brand-name {
    color: var(--ink); font-size: 32px; font-weight: 400;
  }
  .divider {
    position: absolute; left: 292px; top: 24px;
    width: 2px; height: 220px;
    background: linear-gradient(180deg, rgba(120,120,120,0), #8a8a8a 50%, rgba(120,120,120,0));
  }
  .contact {
    position: absolute; left: 328px; top: 40px;
    color: var(--ink);
  }
  .contact .person { font-size: 16px; font-weight: 700; color: var(--ink-strong); }
  .contact .role { font-size: 11px; color: var(--ink-soft); margin-top: 4px; }
  .contact .line {
    display: flex; align-items: center; gap: 10px;
    font-size: 13px; margin-top: 10px;
  }
  .contact .line:first-of-type { margin-top: 16px; }
  .contact .icon {
    width: 20px; height: 20px; border-radius: 50%;
    background: var(--ink-strong);
    display: flex; align-items: center; justify-content: center;
  }
  .contact .address {
    margin-top: 14px; font-size: 13px; font-weight: 700; line-height: 1.35;
    color: var(--ink-strong);
  }
  .front-band { position: absolute; left: 0; bottom: 0; width: 600px; height: 100px; }
  .website {
    position: absolute; left: 28px; bottom: 16px;
    color: var(--white); font-size: 15px; font-weight: 700; letter-spacing: .2px;
  }
</style>
</head>
<body>
<main class="stage">

  <section class="card card-back" aria-label="Card back">
    <div class="back-pattern" role="img" aria-label="Faceted grey geometric background pattern"></div>
    <div class="back-brand">
      <span class="brand-dot"></span>
      <span class="brand-name">Elmfield Dental</span>
    </div>
  </section>

  <section class="card card-front" aria-label="Card front">
    <div class="front-brand">
      <span class="brand-dot"></span>
      <span class="brand-name">Elmfield Dental</span>
    </div>

    <div class="divider"></div>

    <div class="contact">
      <p class="person">Maren Holloway</p>
      <p class="role">Corvel Advisors</p>
      <p class="line">
        <span class="icon">
          <svg width="12" height="12" viewBox="0 0 24 24" aria-hidden="true"><path fill="#fff" d="M6.6 10.8a15 15 0 0 0 6.6 6.6l2.2-2.2c.3-.3.7-.4 1-.2 1.1.4 2.3.6 3.6.6.6 0 1 .4 1 1V20c0 .6-.4 1-1 1A17 17 0 0 1 3 4c0-.6.4-1 1-1h3.5c.6 0 1 .4 1 1 0 1.3.2 2.5.6 3.6.1.3 0 .7-.2 1z"/></svg>
        </span>
        (555) 014-2290
      </p>
      <p class="line">
        <span class="icon">
          <svg width="12" height="12" viewBox="0 0 24 24" aria-hidden="true"><path fill="#fff" d="M2 5h20v14H2z"/><path fill="none" stroke="#5e5e5e" stroke-width="2" d="M2 5l10 8 10-8"/></svg>
        </span>
        mholloway@elmfielddental.com
      </p>
      <p class="address">14-20 Alder Ct<br>Brookvale NY 10990</p>
    </div>

    <svg class="front-band" viewBox="0 0 600 100" aria-hidden="true">
      <path d="M0 58 H224 Q236 58 242 46 L246 40 Q250 34 262 34 H600 V100 H0 Z" fill="var(--band)"/>
      <path d="M0 58 H224 Q236 58 242 46 L246 40 Q250 34 262 34 H600 V38 H262 Q252 38 248 44 L244 50 Q238 62 224 62 H0 Z" fill="var(--band-dark)"/>
    </svg>
    <p class="website">www.elmfielddental.com</p>
  </section>

</main>
</body>
</html>
```